Upmarket Bathroom and Kitchen ware supplier needs a classy business card design

We are a company based in Fiji, we sell plumbing ware (Kitchen and bathroom taps, Basins,showers, toilets etc) through up market show rooms to individuals and directly through Architects and designers of resorts and holiday houses for new builds and renovations. we are wanting to upgrade our over all look and brand. we are starting with a new logo but will be rebranding the whole business. This project is for a business card design for my management and tales team I would like it to be dark, classy and interesting

Target Market(s)

Resort directors and Management, High end holiday home owners

Contact Information for Business Card

Neil Dawson
Director
+64219473815

Colors

Designer to choose colors to be used in the design.

Requirements
Must have
• Must have an upmarket appearance I like darker charcoal shades but will be guided by the designers
• Please any catch phrases like "Crafting remarkable living rooms" this belongs tpo one of our suppliers so can not be used.
Nice to have
• Double sided, so front dedicated to logo provided and back info about the business and the person.

```html
<!DOCTYPE html>
<html lang="en">
<head>
<meta charset="utf-8">
<title>Lagoon Fixtures – Business Card</title>
<link rel="stylesheet" href="https://fonts.googleapis.com/css2?family=Josefin+Sans:wght@300&family=Roboto:wght@400;500&display=swap">
<style>
  :root {
    --backdrop: #8f8f8f;
    --card: #0b0b0b;
    --brand-grey: #a9a9a9;
    --text-light: #e6e6e6;
    --text-muted: #9a9a9a;
    --accent: #e07a1f;
  }
  * { margin: 0; padding: 0; box-sizing: border-box; }
  html, body { width: 1200px; height: 960px; overflow: hidden; }
  body {
    background: var(--backdrop);
    position: relative;
    font-family: "Roboto", Arial, sans-serif;
  }
  .card {
    position: absolute;
    width: 640px;
    height: 366px;
    background: var(--card);
    box-shadow: 0 10px 24px rgba(0,0,0,0.35);
  }
  .card--front { left: 60px; top: 60px; }
  .card--back { left: 500px; top: 534px; }

  .brand-name {
    font-family: "Josefin Sans", "Helvetica Neue", sans-serif;
    font-weight: 300;
    color: var(--brand-grey);
    letter-spacing: 0.38em;
    text-transform: uppercase;
    white-space: nowrap;
  }
  .card--front .brand-name {
    position: absolute;
    left: 0; right: 0; top: 168px;
    text-align: center;
    font-size: 26px;
  }
  .card--back .brand-name {
    position: absolute;
    right: 36px; top: 62px;
    font-size: 17px;
  }

  .holder {
    position: absolute;
    left: 40px; top: 178px;
  }
  .holder__name {
    font-size: 30px;
    font-weight: 500;
    color: var(--text-muted);
    line-height: 1.1;
  }
  .holder__name span { text-transform: uppercase; }
  .holder__role {
    font-size: 17px;
    color: var(--text-muted);
    margin-top: 2px;
  }

  .accent-rule {
    position: absolute;
    left: 0; right: 0; top: 252px;
    height: 2px;
    background: var(--accent);
  }

  .contact {
    position: absolute;
    list-style: none;
    font-size: 16px;
    color: var(--text-light);
  }
  .contact li {
    display: flex;
    align-items: center;
    gap: 8px;
    height: 30px;
  }
  .contact svg { width: 18px; height: 18px; flex: none; }
  .contact--left { left: 40px; top: 266px; }
  .contact--right { right: 30px; top: 266px; }
  .contact--right li { justify-content: flex-end; }
</style>
</head>
<body>

  <section class="card card--front" aria-label="Card front">
    <p class="brand-name">Lagoon Fixtures</p>
  </section>

  <section class="card card--back" aria-label="Card back">
    <p class="brand-name">Lagoon Fixtures</p>

    <div class="holder">
      <p class="holder__name">Neil <span>Dawson</span></p>
      <p class="holder__role">Director</p>
    </div>

    <div class="accent-rule"></div>

    <ul class="contact contact--left">
      <li>
        <svg viewBox="0 0 24 24" aria-hidden="true"><path d="M6.6 3.5l2.6 3.6-1.6 2.3c1 2.3 2.7 4 5 5l2.3-1.6 3.6 2.6-1.3 3.3C11 18.5 5.5 13 4.9 4.8z" fill="none" stroke="var(--accent)" stroke-width="1.8" stroke-linejoin="round"/></svg>
        <span>+64219473815</span>
      </li>
      <li>
        <svg viewBox="0 0 24 24" aria-hidden="true"><rect x="2" y="5" width="20" height="14" fill="var(--accent)"/><path d="M2 5l10 8 10-8" fill="none" stroke="var(--card)" stroke-width="1.6"/></svg>
        <span>info@lagoonfixtures.com</span>
      </li>
    </ul>

    <ul class="contact contact--right">
      <li>
        <span>27 Tavola Street, Navua</span>
        <svg viewBox="0 0 24 24" aria-hidden="true"><path d="M12 2a7 7 0 0 0-7 7c0 5 7 13 7 13s7-8 7-13a7 7 0 0 0-7-7z" fill="var(--accent)"/><circle cx="12" cy="9" r="2.6" fill="var(--card)"/></svg>
      </li>
      <li>
        <span>www.lagoonfixtures.com</span>
        <svg viewBox="0 0 24 24" aria-hidden="true"><circle cx="12" cy="12" r="9.5" fill="none" stroke="var(--accent)" stroke-width="1.8"/><path d="M2.5 12h19M12 2.5c-3.5 3-3.5 16 0 19M12 2.5c3.5 3 3.5 16 0 19" fill="none" stroke="var(--accent)" stroke-width="1.4"/></svg>
      </li>
    </ul>
  </section>

</body>
</html>
```